Brevin Home Care Brochure for Recruiting Clients

I need a brochure made for a home care company called 'Brevin Home Care'. I have uploaded the logo, location, and a few items about our company and what it offers. The final design should communicate trust and respect for patients and their families. I will probably be changing the phone number in the next few days so will need to add a new number and more serving locations.

Industry/Entity Type

Home Health Care

Colors
0555a3
ffffff
3176b5
85acd3
0392cd

Requirements
Must have
• Hello All,
• Thank you kindly for your patience. Please add the changes below to the brochures:
• Phone number: 571-555-0143
• Email: brevinhc@mailnova.test
• Homepage: [Non image link removed]Service Locations: Arlington County, Fairfax County, Fauquier County, Loudoun County, Prince William County
• Also please note the additional sentence at the end of the following key points:
• ABOUT US:
• Brevin serves to give patients the personal care they need in order for them to continue to live dignified and independent lives in the comfort of their homes. We begin by assessing and understanding our patient’s individual needs and met those needs through selectively assigning qualified, trustworthy and compassionate home care aids. Brevin holds great pride in keeping our client’s health, quality of life and well-being central in the design and delivery of our services. Our services can prevent re-hospitalization, postpone institutionalization, and reduce the need for urgent care.
• ABOUT OUR SERVICE PROVIDERS:
• We go through a rigorous in-depth application process with all of our service providers, so that you can rest assure that your home care provider is most qualified to meet your needs. Our application process also includes a thorough screening, criminal background check, DMV driving history and a comprehensive exam. Our service providers are trained, monitored, and tested continuously to meet our high standards of work ethic and professionalism. Our care providers are covered by professional liability, bonding, and workers’ compensation insurance. At Brevin teamwork among members is of key importance and it is how we conduct our day to day business. We work as a team with family, patient and their provider in developing an ideal care plan for the patient.
• OUR SERVICES:
• Companionship Services Include:
• - Offer companionship and conversation - Supervise home maintenance
• - Mail bills and letters
• - Provide reminders for appointments
• - Arrange appointments
• - Maintain calendar
• - Plan visits, outings and trips
• - Visit friends
• - Prepare grocery list
• - Assist with clothing selection
• - Stimulate mental awareness
• - Aid with reading
• - Monitor diet and eating
• - Check food expirations
• - Assist with morning and wake-up
• - Assist with evening and tuck-in
• - Provide respite care
• - Provide medication reminders
• - Assist with walking
• - Write letters and correspondence
• - Organize mail
• - Care for house plants
• - Answer the door
• - Assist with entertaining
• - Play games and cards
• - Rent and play movies
• - Oversee home deliveries
• - Supervise home maintenance
• - Discuss current and historical events - Reminisce about the past
• Home Helper Services Include:
• - Assist with laundry and ironing
• - Organize and clean closets
• - Assist with pet care
• - Attend social and sporting events - Accompany to lunch or dinner
• - Care for Alzhiemers
• - Change linens
• - Dust furniture
• - Drop off and pick up dry cleaning
• - Escort for shopping and errands
• - Escort to appointments
• - Escort to religious services
• - Help with airport task
• - Pick up prescriptions
• - Make beds
• - Prepare meals
• - Plan, prepare, and clean-up meals - Prepare future meals
• - Provide light housekeeping
• - Take out garbage
• Personal Services Include:
• - Ambulation
• - Bathing
• - Cognitive impairment - Mobility
• - Transferring
• - Incontinence
• - Dressing
• - Eating
• - Grooming
Nice to have
• Nice pictures of elderly clients with helpers or nurse.

```html
<!DOCTYPE html>
<html lang="en">
<head>
<meta charset="utf-8">
<title>Brevin Home Care – Our Services</title>
<link rel="stylesheet" href="https://fonts.googleapis.com/css2?family=Didact+Gothic&family=Nunito+Sans:wght@700&display=swap">
<style>
  :root {
    --brand-navy: #0555a3;
    --brand-blue: #3176b5;
    --brand-sky: #85acd3;
    --brand-cyan: #0392cd;
    --panel-top: #b3bcde;
    --panel-bottom: #ffffff;
    --ink: #1d1d1f;
    --paper: #ffffff;
  }
  * { margin: 0; padding: 0; box-sizing: border-box; }
  html, body { width: 1200px; height: 848px; overflow: hidden; background: var(--paper); }
  .spread { position: relative; width: 1200px; height: 848px; overflow: hidden; background: var(--paper); }

  .section-title {
    position: absolute; left: 61px; top: 56px;
    font: 700 14px/1 "Nunito Sans", sans-serif; color: var(--ink); letter-spacing: .2px;
  }

  .service-panel {
    position: absolute;
    border-radius: 14px;
    background: linear-gradient(180deg, var(--panel-top) 0%, #dfe3f2 45%, var(--panel-bottom) 100%);
    padding: 10px 7px;
  }
  .service-panel h2 {
    font: 700 14.5px/1 "Nunito Sans", sans-serif; color: var(--ink);
  }
  .service-list {
    list-style: none;
    font: 15px/21.45px "Didact Gothic", sans-serif; color: var(--ink);
  }
  .service-list li::before { content: "- "; }

  .panel-companion { left: 54px; top: 82px; width: 296px; height: 712px; }
  .panel-companion h2 { margin-bottom: 20px; }
  .panel-helper { left: 455px; top: 82px; width: 296px; height: 470px; }
  .panel-helper h2 { margin-bottom: 15px; }
  .panel-personal { left: 455px; top: 556px; width: 296px; height: 240px; }
  .panel-personal h2 { margin-bottom: 21px; }

  .backdrop-fade {
    position: absolute; left: 0; bottom: 0; width: 802px; height: 190px;
    background: linear-gradient(180deg, rgba(133,172,211,0) 0%, rgba(133,172,211,.35) 60%, rgba(49,118,181,.45) 100%);
    pointer-events: none;
  }

  .photo-area {
    position: absolute; left: 802px; top: 0; width: 398px; height: 848px;
    background:
      linear-gradient(180deg, rgba(255,255,255,0) 60%, rgba(133,172,211,.7) 100%),
      linear-gradient(160deg, #6f9a4a 0%, #a9c68a 28%, #e9ecf2 55%, #d7dfee 80%, #b9c9e2 100%);
  }

  .brand-badge {
    position: absolute; left: 922px; top: 344px;
    display: flex; align-items: center; gap: 8px;
    padding: 10px 12px; border-radius: 22px;
    background: var(--brand-navy);
  }
  .brand-badge .mark { width: 14px; height: 14px; background: var(--paper); }
  .brand-badge .name { font: 700 15px/1.1 "Nunito Sans", sans-serif; color: var(--paper); width: 96px; }
</style>
</head>
<body>
<main class="spread">
  <div class="photo-area" role="img" aria-label="Photo of a smiling senior woman in a wheelchair with a caregiver leaning beside her in a sunny park"></div>
  <div class="brand-badge">
    <span class="mark"></span>
    <span class="name">Brevin Home Care</span>
  </div>

  <div class="backdrop-fade" aria-hidden="true"></div>

  <h1 class="section-title">OUR SERVICES:</h1>

  <section class="service-panel panel-companion">
    <h2>Companionship Services Include:</h2>
    <ul class="service-list">
      <li>Offer companionship and conversation</li>
      <li>Supervise home maintenance</li>
      <li>Mail bills and letters</li>
      <li>Provide reminders for appointments</li>
      <li>Arrange appointments</li>
      <li>Maintain calendar</li>
      <li>Plan visits, outings and trips</li>
      <li>Visit friends</li>
      <li>Prepare grocery list</li>
      <li>Assist with clothing selection</li>
      <li>Stimulate mental awareness</li>
      <li>Aid with reading</li>
      <li>Monitor diet and eating</li>
      <li>Check food expirations</li>
      <li>Assist with morning and wake-up</li>
      <li>Assist with evening and tuck-in</li>
      <li>Provide respite care</li>
      <li>Provide medication reminders</li>
      <li>Assist with walking</li>
      <li>Write letters and correspondence</li>
      <li>Organize mail</li>
      <li>Care for house plants</li>
      <li>Answer the door</li>
      <li>Assist with clothing selection</li>
      <li>Assist with entertaining</li>
      <li>Play games and cards</li>
      <li>Rent and play movies</li>
      <li>Oversee home deliveries</li>
      <li>Supervise home maintenance</li>
      <li>Discuss current and historical events</li>
      <li>Reminisce about the past</li>
    </ul>
  </section>

  <section class="service-panel panel-helper">
    <h2>Home Helper Services Include:</h2>
    <ul class="service-list">
      <li>Assist with laundry and ironing</li>
      <li>Organize and clean closets</li>
      <li>Assist with pet care</li>
      <li>Attend social and sporting events</li>
      <li>Accompany to lunch or dinner</li>
      <li>Care for Alzhiemers</li>
      <li>Change linens</li>
      <li>Dust furniture</li>
      <li>Drop off and pick up dry cleaning</li>
      <li>Escort for shopping and errands</li>
      <li>Escort to appointments</li>
      <li>Escort to religious services</li>
      <li>Help with airport task</li>
      <li>Pick up prescriptions</li>
      <li>Make beds</li>
      <li>Prepare meals</li>
      <li>Plan, prepare, and clean-up meals</li>
      <li>Prepare future meals</li>
      <li>Provide light housekeeping</li>
      <li>Take out garbage</li>
    </ul>
  </section>

  <section class="service-panel panel-personal">
    <h2>Personal Services Include:</h2>
    <ul class="service-list">
      <li>Ambulation</li>
      <li>Bathing</li>
      <li>Cognitive impairment</li>
      <li>Mobility</li>
      <li>Transferring</li>
      <li>Incontinence</li>
      <li>Dressing</li>
      <li>Eating</li>
      <li>Grooming</li>
    </ul>
  </section>
</main>
</body>
</html>
```